business cards

we want our logos on the back
the information on it are on the design I've uploaded
come up with whatever you think is best, we want something professional, sophisticated and sleek.

```html
<!DOCTYPE html>
<html lang="en">
<head>
<meta charset="utf-8">
<title>Kestrel Health and Performance – Business Cards</title>
<link rel="stylesheet" href="https://fonts.googleapis.com/css2?family=Montserrat:wght@400;600;700&display=swap">
<style>
  :root {
    --backdrop: #8f8f8f;
    --card-black: #050505;
    --card-white: #ffffff;
    --brand-green: #4cb648;
    --text-dark: #111111;
    --icon-light: #eaeaea;
  }
  * { box-sizing: border-box; margin: 0; padding: 0; }
  html, body {
    width: 1200px; height: 1200px; overflow: hidden;
    background: var(--backdrop);
    font-family: "Montserrat", Arial, sans-serif;
  }
  .sheet {
    width: 1200px; height: 1200px;
    display: flex; flex-direction: column; align-items: center; justify-content: center;
    gap: 50px;
  }
  .card {
    width: 820px; height: 501px;
    position: relative; overflow: hidden;
    box-shadow: 0 8px 24px rgba(0,0,0,0.25);
  }

  /* Front: brand side */
  .card--front {
    background: var(--card-black);
    display: flex; align-items: center; justify-content: center;
  }
  .brand-name {
    color: var(--card-white);
    font-weight: 600;
    font-size: 34px;
    letter-spacing: 0.02em;
    line-height: 1.2;
    margin-bottom: 40px;
  }

  /* Back: contact side */
  .card--back { background: var(--card-black); display: flex; flex-direction: column; }
  .identity {
    background: var(--card-white);
    height: 188px;
    display: flex; flex-direction: column; align-items: center; justify-content: center;
    gap: 14px; padding-top: 10px;
  }
  .person-name {
    color: var(--text-dark);
    font-weight: 700; font-size: 40px; letter-spacing: 0.06em;
  }
  .person-role {
    color: var(--text-dark);
    font-weight: 400; font-size: 21px; letter-spacing: 0.02em;
  }
  .services {
    background: var(--brand-green);
    height: 40px;
    display: flex; align-items: center; justify-content: center;
    color: var(--card-white);
    font-weight: 400; font-size: 20px; letter-spacing: 0.03em;
  }
  .contacts {
    flex: 1;
    display: grid; grid-template-columns: 1fr 1.25fr;
    padding: 0 40px 0 62px;
    column-gap: 20px;
  }
  .contact-list { list-style: none; display: flex; flex-direction: column; gap: 44px; }
  .contact-list--phones { padding-top: 72px; }
  .contact-list--details { padding-top: 40px; }
  .contact-item {
    display: flex; align-items: center; gap: 16px;
    color: var(--card-white);
    font-weight: 600; font-size: 24px; letter-spacing: 0.02em;
    white-space: nowrap;
  }
  .contact-icon { width: 30px; height: 30px; flex: none; }
</style>
</head>
<body>
<main class="sheet">
  <section class="card card--front" aria-label="Card front">
    <h1 class="brand-name">Kestrel Health and Performance</h1>
  </section>

  <section class="card card--back" aria-label="Card back">
    <header class="identity">
      <h2 class="person-name">MARCUS DELANY</h2>
      <p class="person-role">DIRECTOR - PERSONAL TRAINER - SPORTS NUTRITIONIST</p>
    </header>
    <p class="services">PHYSIO . S&amp;C . COACHING . PERSONAL TRAINING</p>
    <div class="contacts">
      <ul class="contact-list contact-list--phones">
        <li class="contact-item">
          <svg class="contact-icon" viewBox="0 0 30 30" aria-hidden="true">
            <circle cx="15" cy="15" r="15" fill="var(--icon-light)"/>
            <path d="M10 8.5c1-.6 1.8-.4 2.3.5l1.2 2.3c.4.8.2 1.5-.5 2l-.8.6c.8 1.8 2 3 3.8 3.9l.6-.8c.5-.7 1.3-.9 2-.5l2.3 1.2c.9.5 1.1 1.3.5 2.3l-.6.9c-.7 1-2 1.4-3.3.9-3.9-1.5-6.7-4.3-8.2-8.2-.5-1.3-.1-2.6.9-3.3z" fill="var(--card-black)"/>
          </svg>
          <span>03 9000 1478</span>
        </li>
        <li class="contact-item">
          <svg class="contact-icon" viewBox="0 0 30 30" aria-hidden="true">
            <circle cx="15" cy="15" r="15" fill="var(--icon-light)"/>
            <path d="M10 8.5c1-.6 1.8-.4 2.3.5l1.2 2.3c.4.8.2 1.5-.5 2l-.8.6c.8 1.8 2 3 3.8 3.9l.6-.8c.5-.7 1.3-.9 2-.5l2.3 1.2c.9.5 1.1 1.3.5 2.3l-.6.9c-.7 1-2 1.4-3.3.9-3.9-1.5-6.7-4.3-8.2-8.2-.5-1.3-.1-2.6.9-3.3z" fill="var(--card-black)"/>
          </svg>
          <span>03 9000 3391</span>
        </li>
      </ul>
      <ul class="contact-list contact-list--details">
        <li class="contact-item">
          <svg class="contact-icon" viewBox="0 0 30 30" aria-hidden="true">
            <circle cx="15" cy="15" r="15" fill="var(--icon-light)"/>
            <rect x="8" y="10" width="14" height="10" rx="1.5" fill="none" stroke="var(--card-black)" stroke-width="1.8"/>
            <path d="M8.5 11l6.5 5 6.5-5" fill="none" stroke="var(--card-black)" stroke-width="1.8"/>
          </svg>
          <span>hello@kestrelfitness.com.au</span>
        </li>
        <li class="contact-item">
          <svg class="contact-icon" viewBox="0 0 30 30" aria-hidden="true">
            <circle cx="15" cy="15" r="15" fill="var(--icon-light)"/>
            <path d="M15 7a5.5 5.5 0 0 0-5.5 5.5c0 4 5.5 10 5.5 10s5.5-6 5.5-10A5.5 5.5 0 0 0 15 7z" fill="var(--card-black)"/>
            <circle cx="15" cy="12.5" r="2.1" fill="var(--icon-light)"/>
          </svg>
          <span>27 Linden Rd, Northvale</span>
        </li>
      </ul>
    </div>
  </section>
</main>
</body>
</html>
```